Wordpress Business Travel Blog and Discussion Board

Oh, Hello!

We are looking for a motivated designer to create a full, turnkey interactive WordPress website geared toward business travel that includes a news style blog (look at ByteHarbor.com and Wirevane.com for the style we like) that is seamlessly integrated with a robust message board (look at JetGabble.com and LoftCabin.com). Ok, so stick with us here because this is actually a pretty cool project that shouldn't be too hard, but yes, of course we have some curve balls that we are throwing your way. Sorry! :)

*On the front page*

- We would like to have a typical news style blog layout that is fun, somewhat professional, and easy to read. That's easy!

- Somewhere within first glance, we would like to have a short list of the most active discussions on our discussion board. (What's trending, or something like that). Not too bad, right?

- Overall, want to have a good amount of content, but we also do not want the visitor to feel as if he or she is having to sift through a lot of content to see what he or she wants to see. Great! We're past the beginning!

We will have traditional visual advertising on all of our pages. Please leave space as necessary :)

*On the Blog/News story pages*

Let's keep these simple - but there is a twist!

Let's say I create a blog/news post. I would like that blog/news post to also be opened as a discussion on the discussion board. For example, I write an article about Corvane Airways and their service on a particular international flight. This will be opened as a discussion under the Corvane Airways topic in the discussion board. Other users can also open new discussions under any topic on the discussion board, but they cannot post stories (unless permission is given) to the blog wall. We would like their posts to show up as regular discussion board posts while the news/blog posts by us show up as news/blog posts on the front page, *and* (oh yes we did!) as discussions in the discussion board. Of course, users will still be able to post comments to the news/blog post, which will also be posted in the discussion.

OK, does that make sense? Let me know if I can help make this more clear! :) Sorry!

*Wiki Pages*

Take a look at the Corvane Airways example above. In that example, my news/blog entry automatically opens a new discussion post. Although we won't necessarily need to create a new wiki page, we would like to tag the post and the discussion to a wiki page about the topic. The wiki page can be created and edited by all users (and locked by us if necessary). BONUS! Can we tag more than one wiki page?

*Websites that inspire us*

ByteHarbor.com - concept and design
Wirevane.com - concept and design
JetGabble.com - concept
LoftCabin.com - concept
pomwhisper.com - concept

All of the sites above are great and we can only thrive with their great success. We are not aiming to be a competitor to the travel sites, but just another great option for interested visitors. Please do not simply copy what they have. What is posted above is a list of our favorite sites that we visit every day.

Our favorite font is Segoe UI, but please don't use this (or a similar font) too much! Maybe just titles would be great. You're the designer so you can make the call here.

Also, our favorite color is blue, but if you have another favorite color, go ahead and show us what you can do! (Don't use too much blue!)

*Oh, and One More Thing*

(I know, you thought we were done. We're not!)

Here's the killer - We would like to create a way for people to, say, enter the details of their next trip and be matched with someone who will also be on a portion of their trip.

For example, let's say I am flying Brisola Airways flight 109 from Los Angeles to New York JFK Airport this Friday. I am staying at the Marrow Lodge Manhattan Central on Friday night, and I am flying back on Saturday night on Quessa flight 290 from New York JFK airport back to Los Angeles. Another user will also be on the Quessa flight back to Los Angeles with me and he entered that information in the website. (Note, the user has to manually enter this information). The other user and I will both be notified that there is at least one other user who will be on the same Quessa flight as me. We will both have the option to reveal our online identity - which will in fact be released to each person as long as each person *mutually* agrees.

This can be very simple - almost like a dating site type of match but it is based on two people being in the same place at the same time (based on what they report). Also, we would like to be able to collect this information - not necessarily tied to the user's true identity. The information we would like to have is - what the user is claiming he or she is doing on the trip (i.e. staying at the Marrow Lodge Central, flying Brisola Airways), and whether or not the user agreed to reveal his or her identity - AND! whether or not the users both revealed their identity.

*Most Important*

HAVE FUN and THANK YOU!! :)

A couple of quick notes - this is a design and code project. We are most likely offering a more $(!) design and code project for the version 2.0 of this website once we get user feedback from this first round.

Also, the name of the website is Veyrola. (www.veyrola.com)

Good luck!

• We need to have a high end, professional, modern, and clean design on the front page to entice readers to constantly visit and stay on our site.
• It would be great to give us the ability to automatically recognize users for visiting the website and/or participating and commenting. Social badges, recognition, etc. would be very cool.
• Although this is a website around business travel, we do not necessarily want it to be business travel themed. There can be hints of the theme, but otherwise the visual look should be somewhat generic.

```html
<!DOCTYPE html>
<html lang="en">
<head>
<meta charset="utf-8">
<title>Veyrola — Business Travel Blog</title>
<link rel="stylesheet" href="https://fonts.googleapis.com/css2?family=Open+Sans:wght@400;600;700&family=Lato:wght@400;700&display=swap">
<style>
:root{
  --navy:#1b3f8e;
  --navy-dark:#12306f;
  --link:#1f63b0;
  --accent:#1e7bc4;
  --steel:#6b93a8;
  --steel-dark:#557d93;
  --panel:#eef2f5;
  --line:#d5dde3;
  --text:#222;
  --muted:#666;
  --red:#e0301e;
  --orange:#f39a1f;
  --footer-grey:#dadde0;
  --promo-text:#e8dcc4;
}
*{box-sizing:border-box;margin:0;padding:0}
html,body{width:1200px;height:2219px;overflow:hidden;background:#fff}
body{position:relative;font-family:"Lato",Arial,sans-serif;color:var(--text);font-size:12px}
.abs{position:absolute}
a{color:inherit;text-decoration:none}

/* top bar */
.topbar{left:0;top:0;width:1200px;height:34px;background:linear-gradient(#2250a6,var(--navy-dark))}
.topbar .links{left:140px;top:0;height:34px;display:flex;gap:16px;align-items:center;color:#fff;font-size:12px;font-weight:700}
.topbar .auth{right:142px;top:2px;display:flex;gap:4px}
.btn-top{height:30px;padding:0 14px;display:flex;align-items:center;gap:6px;background:linear-gradient(#3a7fd6,#1f5db4);color:#fff;font-size:12px;border:1px solid #5d97e0}
.mainnav{left:140px;top:34px;width:920px;height:33px;display:flex;border-bottom:2px solid #cfe0f1}
.mainnav a{flex:1;text-align:center;line-height:33px;color:var(--link);font-size:14px;font-family:"Open Sans",sans-serif;border-right:1px solid #c8d9ea}
.mainnav a:last-child{border-right:0}

/* header */
.promo{left:140px;top:74px;width:685px;height:87px;background:linear-gradient(90deg,#1c1c1c,#3b3b3b 50%,#1c1c1c);color:#ddd}
.promo .left{left:22px;top:30px;font-size:10px;line-height:14px;text-align:right}
.promo .event{left:196px;top:14px;width:272px;text-align:center;color:var(--promo-text);font-family:"Lato",sans-serif;font-weight:700}
.promo .event small{display:block;font-size:10px;letter-spacing:1px;line-height:14px}
.promo .event b{display:block;font-size:22px;line-height:26px;letter-spacing:1px;font-weight:700}
.promo .right{left:532px;top:30px;font-size:10px;line-height:14px;letter-spacing:1px}
.follow{left:834px;top:76px;display:flex;align-items:center;gap:5px;font-size:11px;color:#333}
.sq{width:22px;height:22px;border-radius:4px}
.search{left:836px;top:112px;width:224px;height:29px;border:1px solid #ccc;display:flex}
.search span{flex:1;padding:6px 8px;color:#888;font-size:12px}
.search i{width:29px;background:var(--red);display:flex;align-items:center;justify-content:center}
.site-row{left:836px;top:150px;width:224px;display:flex;justify-content:space-between;font-size:11px;color:#333}
.hero{left:140px;top:166px;width:920px;height:112px;background:linear-gradient(90deg,#5bb4e6,#a9dcf4 45%,#5aa6d9)}
.hero .brand{left:20px;top:20px;font-family:"Open Sans",sans-serif;font-weight:700;font-size:58px;color:#1f8fd9;line-height:70px}
.hero .plane{left:420px;top:0;width:340px;height:112px;background:linear-gradient(120deg,rgba(255,255,255,0),rgba(255,255,255,.55),rgba(210,225,240,.2))}

/* feature */
.feature{left:140px;top:287px;width:609px;height:346px;background:var(--steel)}
.feature h2{left:15px;top:10px;width:300px;color:#fff;font-family:"Open Sans",sans-serif;font-size:19px;line-height:22px;font-weight:700}
.video{left:15px;top:58px;width:298px;height:206px;background:linear-gradient(135deg,#f2b8b4,#e9e4dc 50%,#d8564b)}
.vctrl{left:15px;top:264px;width:298px;height:28px;background:#e8ecef;display:flex;align-items:center;gap:8px;padding:0 8px;font-size:11px;color:#333}
.vctrl .bar{flex:1;height:4px;background:#bbb;position:relative}
.vctrl .bar::before{content:"";position:absolute;left:0;top:0;width:60%;height:4px;background:var(--accent)}
.highlights{left:322px;top:0;width:280px}
.highlights h3{color:#fff;font-family:"Open Sans",sans-serif;font-size:16px;font-weight:700;padding:12px 0 4px 2px;border-bottom:1px solid #a6c0cf}
.hl-item{position:absolute;left:0;width:280px;height:77px;background:var(--panel);border-radius:3px;display:flex;gap:10px;padding:10px 8px}
.hl-item .thumb{width:82px;height:58px;flex:none}
.hl-item p{font-size:13px;line-height:16px;color:#333}
.viewall{right:14px;top:312px;color:#fff;font-family:"Open Sans",sans-serif;font-weight:700;font-size:15px}

/* sidebar */
.sidebar{left:750px;top:286px;width:310px;height:1340px;background:var(--steel)}
.ad{left:758px;top:292px;width:294px;height:244px;background:var(--orange);border:1px solid #d37b00}
.ad .txt{left:0;top:18px;width:294px;text-align:center;font-family:"Open Sans",sans-serif;font-weight:700;color:#1a1a1a;font-size:24px;line-height:27px}
.ad .person{left:10px;top:140px;width:110px;height:100px;background:linear-gradient(#f7c37a,#bf8d4d)}
.ad .roll{left:126px;top:150px;font-size:15px;font-weight:700;color:#111}
.ad .logo{left:140px;top:190px;width:140px;height:44px;background:#fff;border-radius:4px;text-align:center}
.ad .logo b{display:block;font-size:16px;color:#222;line-height:24px}
.ad .logo small{font-size:9px;color:#333}
.card{position:absolute;left:758px;width:294px;background:#fff;overflow:hidden}
.card h4{color:var(--link);font-family:"Open Sans",sans-serif;font-weight:700;font-size:14px;padding:8px 10px;border-bottom:1px solid var(--line)}
.match .row{display:flex;align-items:center;padding:0 10px;height:32px;font-size:12px;color:#333}
.match .row span{width:100px}
.match .field{width:126px;height:20px;border:1px solid #bbb}
.btn{background:var(--accent);color:#fff;font-size:12px;font-weight:700}
.tabs{display:flex;height:46px;border-bottom:1px solid var(--line)}
.tabs div{flex:1;padding:6px 12px;font-size:13px;line-height:15px;color:#888;background:#f0f2f4;border-left:1px solid var(--line)}
.tabs div.on{background:#fff;color:var(--accent);border-left:0;border-bottom:2px solid var(--accent)}
.trend{display:flex;gap:12px;padding:13px 10px 13px 20px;border-bottom:1px solid var(--line);height:93px}
.trend .thumb{width:86px;height:66px;flex:none;background:linear-gradient(135deg,#c7d8e6,#f4f7fa 60%,#2e3e58)}
.trend p{font-size:14px;line-height:16px;color:#222}
.news-row{display:flex;margin:16px 10px;height:32px}
.news-row .in{flex:1;border:1px solid #bbb;padding:7px 8px;color:#555;font-size:12px}
.news-row .btn{width:86px;display:flex;align-items:center;justify-content:center;font-weight:400}
.soc-like{display:flex;align-items:center;gap:8px;margin:26px 0 0 20px;font-size:9px;color:#555;width:260px}
.pill{border:1px solid #aaa;border-radius:3px;background:#f3f3f3;padding:2px 6px;font-size:11px;color:#333;display:flex;align-items:center;gap:4px;white-space:nowrap}
.pill i{width:10px;height:10px;background:var(--accent);border-radius:2px;display:inline-block}
.soc-icons{display:flex;gap:14px;margin:38px 0 0 20px}
.soc-icons div{width:40px;height:40px;border-radius:6px}

/* posts */
.post{position:absolute;left:155px;width:586px}
.share-col{position:absolute;left:0;top:0;width:70px}
.bubble{width:60px;height:24px;border-radius:12px;background:var(--steel);color:#fff;font-size:12px;font-weight:700;display:flex;align-items:center;justify-content:center;gap:6px;margin-bottom:6px}
.bubble i{width:16px;height:12px;background:#fff;border-radius:3px}
.srow{display:flex;align-items:center;gap:4px;margin-bottom:8px}
.sbtn{height:18px;padding:0 5px;border:1px solid #bbb;border-radius:2px;background:#f5f5f5;font-size:10px;display:flex;align-items:center;gap:3px;color:#333}
.sbtn i{width:10px;height:10px;display:inline-block}
.cnt{height:18px;padding:0 4px;border:1px solid #ccc;font-size:9px;line-height:16px;color:#444}
.post-body{position:absolute;left:113px;top:0;width:473px}
.meta{font-size:10px;color:#333;line-height:12px}
.meta b{color:var(--link);font-weight:400;text-transform:uppercase}
.post h2{font-family:"Open Sans",sans-serif;font-size:29px;line-height:31px;font-weight:700;color:#111;margin:6px 0 16px}
.lead{display:flex;gap:14px}
.lead .photo{width:200px;height:159px;flex:none}
.post p{font-size:12.5px;line-height:18px;color:#555}
.post p.full{margin-top:14px}
.more{color:var(--link);font-weight:700;font-size:12px}
.divider{position:absolute;left:155px;width:586px;height:1px;background:var(--line)}
.nextbar{left:155px;top:2093px;width:586px;height:32px;background:linear-gradient(var(--accent),#1668ad);color:#fff;text-align:right;padding:2px 14px;font-family:"Open Sans",sans-serif;font-weight:700;font-size:20px}

/* footer */
.foot-nav{left:140px;top:2135px;width:920px;height:25px;background:var(--footer-grey);display:flex;align-items:center;gap:30px;padding-left:22px;font-size:12px;color:#222}
.foot-nav .sqs{margin-left:auto;margin-right:20px;display:flex;gap:8px}
.foot-bottom{left:140px;top:2160px;width:920px;height:50px;background:linear-gradient(#2250a6,var(--navy-dark));color:#fff;display:flex;align-items:center;padding:0 16px}
.foot-bottom .brand{font-family:"Open Sans",sans-serif;font-weight:700;font-size:26px}
.foot-bottom .legal{margin-left:auto;display:flex;gap:18px;font-size:12px}
</style>
</head>
<body>

<header>
  <div class="abs topbar">
    <nav class="abs links"><a>BLOG</a><a>FORUMS</a><a>MEMBERS</a><a>WIKI</a><a>HELP</a></nav>
    <div class="abs auth">
      <a class="btn-top"><svg width="11" height="11" viewBox="0 0 11 11"><circle cx="5.5" cy="3" r="2.6" fill="#fff"/><path d="M0 11c0-4 11-4 11 0z" fill="#fff"/></svg>Register Now</a>
      <a class="btn-top"><svg width="11" height="11" viewBox="0 0 11 11"><circle cx="7" cy="4" r="3" fill="none" stroke="#fff" stroke-width="1.6"/><path d="M5 6 1 10" stroke="#fff" stroke-width="1.8"/></svg>Login</a>
    </div>
  </div>
  <nav class="abs mainnav">
    <a>HOME</a><a>MILES &amp; POINTS</a><a>TRAVEL &amp; DINING</a><a>COMMUNITY</a><a>OMNI</a><a>DESTINATIONS</a><a>CONTACT US</a>
  </nav>

  <aside class="abs promo" aria-label="Advertisement">
    <div class="abs left">REGISTER BY JANUARY 31<br>FOR A SPECIAL RATE</div>
    <div class="abs event"><small>CORLIN STYLE MEDIA</small><b>TAILORED TRADE<br>FORUM</b></div>
    <div class="abs right">APRIL 12, 2012<br>LAKEPORT</div>
  </aside>
  <div class="abs follow">FOLLOW US
    <div class="sq" style="background:#3b5b9a"></div><div class="sq" style="background:#3fa9dd"></div><div class="sq" style="background:#1f75b0"></div><div class="sq" style="background:#d42a1f"></div><div class="sq" style="background:#f07c1c"></div>
  </div>
  <div class="abs search"><span>Search</span><i><svg width="12" height="12" viewBox="0 0 12 12"><circle cx="5" cy="5" r="3.6" fill="none" stroke="#fff" stroke-width="1.8"/><path d="M7.6 7.6 11 11" stroke="#fff" stroke-width="2"/></svg></i></div>
  <div class="abs site-row"><span>www.veyrola.com</span><span>SUBSCRIBE</span></div>

  <div class="abs hero">
    <div class="abs brand">Veyrola</div>
    <div class="abs plane" role="img" aria-label="Photo of a jet airliner flying above clouds"></div>
  </div>
</header>

<section class="abs feature">
  <h2 class="abs">Nullam ac lectus nisi, id commodo sem.</h2>
  <div class="abs video" role="img" aria-label="Video still of a family with luggage boarding an airplane"></div>
  <div class="abs vctrl">
    <svg width="10" height="10" viewBox="0 0 10 10"><path d="M1 0 9 5 1 10z" fill="#333"/></svg>
    <svg width="12" height="10" viewBox="0 0 12 10"><path d="M0 3h3l4-3v10L3 7H0z" fill="#333"/></svg>
    <div class="bar"></div><span>42:15</span><span>Share</span>
    <svg width="10" height="10" viewBox="0 0 10 10"><rect x="0.5" y="0.5" width="9" height="9" fill="none" stroke="#333"/></svg>
  </div>
  <div class="abs highlights">
    <h3>HIGHLIGHTS</h3>
    <div class="hl-item" style="top:40px"><div class="thumb" role="img" aria-label="Airport terminal interior" style="background:linear-gradient(135deg,#9fb9d4,#e6eef5)"></div><p>Lorem ipsum dolor sit amet, consectetur adipiscing elit.</p></div>
    <div class="hl-item" style="top:131px"><div class="thumb" role="img" aria-label="Business traveller on a phone" style="background:linear-gradient(135deg,#6c7d92,#cdd6e0)"></div><p>Maecenas sit amet massa metus, id semper diam.</p></div>
    <div class="hl-item" style="top:218px"><div class="thumb" role="img" aria-label="Traveller working on a laptop" style="background:linear-gradient(135deg,#8b7b6d,#e7e1da)"></div><p>Donec feugiat ligula non odio ullamcorper nec luctus turpis vehicula.</p></div>
  </div>
  <a class="abs viewall">View all videos ›</a>
</section>

<div class="abs sidebar"></div>
<aside class="abs ad" aria-label="Advertisement">
  <div class="abs txt">ANVIKA RAO IS A<br>BUSINESS PIONEER<br><span style="font-size:22px">WHAT ABOUT YOU?</span></div>
  <div class="abs person" role="img" aria-label="Portrait of a businesswoman"></div>
  <div class="abs roll">&lt;&lt;Rollover</div>
  <div class="abs logo"><b>Tallstone</b><small>Domains, Websites and more...</small></div>
</aside>

<section class="card match" style="top:546px;height:142px">
  <h4>MATCH A PORTION ON YOUR TRIP!</h4>
  <div class="row" style="margin-top:6px"><span>Start Date</span><div class="field"></div>
    <svg style="margin-left:10px" width="18" height="16" viewBox="0 0 18 16"><rect x="1" y="2" width="16" height="13" fill="#5aa6e0"/><rect x="3" y="6" width="12" height="7" fill="#fff"/></svg></div>
  <div class="row"><span>Flight Number</span><div class="field"></div>
    <svg style="margin-left:6px" width="26" height="12" viewBox="0 0 26 12"><path d="M1 6h24M12 1l4 5-4 5" stroke="#555" stroke-width="1.4" fill="none"/></svg></div>
  <div class="row"><span></span><div class="btn" style="padding:3px 10px">Search</div></div>
</section>

<section class="card" style="top:699px;height:531px">
  <div class="tabs"><div class="on">Recent Trending</div><div>Archieve Trending</div><div>All Trending</div></div>
  <div class="trend"><div class="thumb" role="img" aria-label="Businessman in an airport"></div><p>Maecenas sit amet massa metus, id semper diam.</p></div>
  <div class="trend"><div class="thumb" role="img" aria-label="Businessman in an airport"></div><p>Maecenas sit amet massa metus, id semper diam.</p></div>
  <div class="trend"><div class="thumb" role="img" aria-label="Businessman in an airport"></div><p>Maecenas sit amet massa metus, id semper diam.</p></div>
  <div class="trend"><div class="thumb" role="img" aria-label="Businessman in an airport"></div><p>Maecenas sit amet massa metus, id semper diam.</p></div>
  <div class="trend" style="border-bottom:0"><div class="thumb" role="img" aria-label="Businessman in an airport"></div><p>Maecenas sit amet massa metus, id semper diam.</p></div>
</section>

<section class="card" style="top:1239px;height:96px">
  <h4>NEWSLETTERS</h4>
  <div class="news-row"><div class="in">Enter your e-mail address</div><div class="btn">Subscribe</div></div>
</section>

<section class="card" style="top:1346px;height:278px">
  <h4>SOCIALIZE</h4>
  <div class="soc-like"><div class="pill"><i></i>Like</div><span>498,909 people like this. Sign Up to see what your friends like.</span></div>
  <div style="height:1px;background:var(--line);margin:22px 10px 0"></div>
  <div class="soc-like" style="margin-top:20px"><div class="pill" style="padding:4px 8px"><i></i>Follow @Veyrola</div><div class="pill" style="padding:4px 8px">2.3M followers</div></div>
  <div style="height:1px;background:var(--line);margin:18px 10px 0"></div>
  <div class="soc-icons" style="margin-top:22px">
    <div style="background:#3b5b9a"></div><div style="background:#3fa9dd"></div><div style="background:#1f75b0"></div><div style="background:#d42a1f"></div><div style="background:#f07c1c"></div>
  </div>
</section>

<main>
  <article class="post" style="top:647px">
    <div class="share-col">
      <div class="bubble"><i></i>18</div>
      <div class="srow"><span class="sbtn"><i style="background:#3b5b9a"></i>Like</span><span class="cnt">251</span></div>
      <div class="srow"><span class="sbtn"><i style="background:#3fa9dd"></i>Post</span><span class="cnt">483</span></div>
      <div class="srow"><span class="sbtn"><i style="background:#1f75b0"></i>Share</span><span class="cnt">21</span></div>
      <div class="srow"><span class="sbtn"><i style="background:#d42a1f"></i>+1</span><span class="cnt">17</span></div>
    </div>
    <div class="post-body">
      <div class="meta"><b>Dana Holt</b><br>posted 51 mins ago</div>
      <h2>Fusce commodo ligula consequat lacus venenatis congue condimentum neque auctor.</h2>
      <div class="lead">
        <div class="photo" role="img" aria-label="Airliner taking off against a sunset sky" style="background:linear-gradient(160deg,#6f7f96,#e6d8c4 60%,#3d4556)"></div>
        <p>Sed ut perspiciatis unde omnis iste natus error sit voluptatem accusantium doloremque laudantium, totam rem aperiam, eaque ipsa quae ab illo inventore veritatis et quasi architecto beatae vitae dicta sunt explicabo. Nemo enim ipsam voluptatem quia voluptas sit aspernatur aut odit aut fugit, sed quia consequuntur magni dolores eos qui</p>
      </div>
      <p class="full">Sed ut perspiciatis unde omnis iste natus error sit voluptatem accusantium doloremque laudantium, totam rem aperiam, eaque ipsa quae ab illo inventore veritatis et quasi architecto beatae vitae dicta sunt explicabo. Nemo enim ipsam voluptatem quia voluptas sit aspernatur aut odit aut fugit, sed quia consequuntur magni dolores eos qui ratione voluptatem sequi nesciunt. Neque porro quisquam est, qui dolorem <a class="more">⟶ Read More</a></p>
    </div>
  </article>
  <div class="divider" style="top:1120px"></div>

  <article class="post" style="top:1146px">
    <div class="share-col">
      <div class="bubble"><i></i>6</div>
      <div class="srow"><span class="sbtn"><i style="background:#3b5b9a"></i>Like</span><span class="cnt">251</span></div>
      <div class="srow"><span class="sbtn"><i style="background:#3fa9dd"></i>Post</span><span class="cnt">483</span></div>
      <div class="srow"><span class="sbtn"><i style="background:#1f75b0"></i>Share</span><span class="cnt">21</span></div>
      <div class="srow"><span class="sbtn"><i style="background:#d42a1f"></i>+1</span><span class="cnt">17</span></div>
    </div>
    <div class="post-body">
      <div class="meta"><b>Lena Marsh</b><br>posted yesterday</div>
      <h2>Donec volutpat dapibus lacus, in convallis magna aliquam in.</h2>
      <div class="lead">
        <div class="photo" role="img" aria-label="Travellers on an airport moving walkway" style="background:linear-gradient(160deg,#cfe0ee,#8aa3bb 55%,#3e4a5a)"></div>
        <p>Sed ut perspiciatis unde omnis iste natus error sit voluptatem accusantium doloremque laudantium, totam rem aperiam, eaque ipsa quae ab illo inventore veritatis et quasi architecto beatae vitae dicta sunt explicabo. Nemo enim ipsam voluptatem quia voluptas sit aspernatur aut odit aut fugit, sed quia consequuntur magni dolores eos qui ratione voluptatem sequi nesciunt. Neque porro quisquam <a class="more">⟶ Read More</a></p>
      </div>
    </div>
  </article>
  <div class="divider" style="top:1494px"></div>

  <article class="post" style="top:1516px">
    <div class="share-col">
      <div class="bubble"><i></i>6</div>
      <div class="srow"><span class="sbtn"><i style="background:#3b5b9a"></i>Like</span><span class="cnt">251</span></div>
      <div class="srow"><span class="sbtn"><i style="background:#3fa9dd"></i>Post</span><span class="cnt">483</span></div>
      <div class="srow"><span class="sbtn"><i style="background:#1f75b0"></i>Share</span><span class="cnt">21</span></div>
      <div class="srow"><span class="sbtn"><i style="background:#d42a1f"></i>+1</span><span class="cnt">17</span></div>
    </div>
    <div class="post-body">
      <div class="meta"><b>Lena Marsh</b><br>posted yesterday</div>
      <h2>Phasellus consectetur erat nec tortor lobortis sed vestibulum massa tristique.</h2>
      <div style="position:relative;width:463px;height:284px;background:linear-gradient(150deg,#dfe4e8,#b9c2ca 50%,#4d5560)" role="img" aria-label="Video still of two business travellers with a laptop in an airport lounge">
        <div style="position:absolute;left:0;bottom:0;width:463px;height:42px;background:rgba(0,0,0,.55);display:flex;align-items:center;gap:16px;padding-left:110px;color:#fff;font-size:12px">
          <svg width="14" height="16" viewBox="0 0 14 16"><path d="M0 0 14 8 0 16z" fill="#fff"/></svg>Sed ut perspiciatis unde omnis</div>
      </div>
      <p class="full">Sed ut perspiciatis unde omnis iste natus error sit voluptatem accusantium doloremque laudantium, totam rem aperiam, eaque ipsa quae ab illo inventore veritatis et quasi architecto beatae vitae dicta sunt explicabo. Nemo enim ipsam voluptatem quia voluptas sit aspernatur aut odit aut fugit, sed quia consequuntur magni dolores eos qui ratione voluptatem sequi nesciunt. Neque porro quisquam <a class="more">⟶ Read More</a></p>
    </div>
  </article>

  <a class="abs nextbar">Next ›</a>
</main>

<footer>
  <nav class="abs foot-nav"><a>Home</a><a>Blog</a><a>Forums</a><a>Members</a><a>Wiki</a><a>Help</a>
    <span class="sqs"><i style="width:12px;height:12px;background:#222;display:block"></i><i style="width:12px;height:12px;background:#222;display:block"></i></span></nav>
  <div class="abs foot-bottom">
    <span class="brand">Veyrola</span>
    <div class="legal"><a>Privacy Policy</a><span>|</span><a>Terms Of Service</a><span>|</span><span>© 2012 Veyrola. All rights reserved.</span></div>
  </div>
</footer>

</body>
</html>
```